Summit Brightway Realty Group & Greenleaf Lending Services, Inc.
Present Our
Annual Holiday Celebration

for Agents, Originators, Clients & Friends
All are Welcome!!

Catered by Chef Ramo Ramo
w/ DJ and Full Dance Floor

** No Cover Charge
Saturday, January 22, 2022
7 pm - 11 pm

at Velvet Parlor
4871 Q Street NE Washington DC 20019

Call Marcus Pelletier at (240) 555-0184 with questions.

```html
<!DOCTYPE html>
<html lang="en">
<head>
<meta charset="utf-8">
<title>Annual Holiday Celebration</title>
<link rel="stylesheet" href="https://fonts.googleapis.com/css2?family=Oswald:wght@500&family=Montserrat:wght@400;500;600;700&family=Pacifico&display=swap">
<style>
  :root {
    --sky: #b9dfe8;
    --sky-light: #cfeaf0;
    --teal: #3a6373;
    --red: #c01f2e;
    --pine-dark: #4a78cc;
    --pine-light: #86abe4;
    --photo-warm: #c9b8a2;
    --photo-cool: #8c7b6c;
  }
  * { margin: 0; padding: 0; box-sizing: border-box; }
  html, body { width: 1200px; height: 1200px; overflow: hidden; background: #fff; }
  .invite {
    position: relative; width: 1200px; height: 1200px; overflow: hidden;
    background: radial-gradient(ellipse at 50% 55%, var(--sky-light), var(--sky) 75%);
    font-family: "Montserrat", sans-serif; color: var(--teal);
  }
  .garland { position: absolute; left: 0; top: 0; width: 1200px; height: 440px; }
  .line { position: absolute; left: 0; width: 1200px; text-align: center; white-space: nowrap; }
  .hosts { top: 298px; font-family: "Oswald", sans-serif; font-weight: 500; font-size: 29px; letter-spacing: 0.5px; }
  .presents { top: 340px; font-weight: 700; font-size: 25px; letter-spacing: 25px; color: var(--red); padding-left: 25px; }
  .annual { top: 388px; font-weight: 500; font-size: 77px; letter-spacing: 2px; line-height: 1; }
  .holiday { top: 428px; font-family: "Pacifico", cursive; font-size: 165px; color: var(--red); line-height: 1.3; padding-left: 20px; }
  .celebration { top: 672px; font-weight: 400; font-size: 63px; letter-spacing: 1px; line-height: 1; }
  .rule { position: absolute; left: 183px; width: 862px; height: 2px; background: var(--red); }
  .rule.top { top: 757px; }
  .rule.bottom { top: 838px; }
  .audience { top: 767px; font-weight: 500; font-size: 25px; letter-spacing: 1.5px; line-height: 35px; }
  .catering { top: 862px; font-weight: 500; font-size: 21px; letter-spacing: 1.5px; }
  .catering .chef { color: var(--red); font-weight: 700; }
  .music { top: 893px; font-weight: 500; font-size: 25px; letter-spacing: 1px; }
  .admission { top: 939px; left: -22px; font-weight: 700; font-size: 41px; color: var(--red); }
  .admission .stars { display: inline-block; width: 14px; font-size: 11px; line-height: 11px; vertical-align: middle; margin: 0 16px; white-space: normal; }
  .venue { top: 990px; left: -7px; font-weight: 500; font-size: 22px; letter-spacing: 0.8px; }
  .date { top: 1015px; left: -9px; font-weight: 700; font-size: 25px; letter-spacing: 1px; color: var(--red); }
  .date .star { font-size: 13px; vertical-align: middle; margin: 0 14px; }
  .partner { position: absolute; top: 1092px; display: flex; align-items: center; gap: 8px; font-weight: 700; font-size: 15px; line-height: 1.15; color: var(--teal); }
  .partner .dot { width: 14px; height: 14px; border-radius: 50%; background: var(--teal); flex: none; }
  .partner.lending { left: 86px; width: 160px; }
  .partner.realty { left: 264px; width: 180px; }
  .contact { position: absolute; left: 471px; top: 1058px; }
  .contact .name { font-weight: 700; font-size: 38px; color: var(--red); letter-spacing: 0.5px; line-height: 1.2; }
  .contact .phone { font-weight: 700; font-size: 22.5px; letter-spacing: 0.5px; margin-top: 4px; }
  .chef-photo { position: absolute; left: 906px; top: 853px; width: 294px; height: 347px; }
</style>
</head>
<body>
<main class="invite">
  <svg class="garland" viewBox="0 0 1200 440" role="img" aria-label="Blue pine branches with gold ribbons and striped gold ornaments">
    <defs>
      <linearGradient id="pine" x1="0" y1="0" x2="0" y2="1">
        <stop offset="0" stop-color="var(--pine-dark)"/>
        <stop offset="1" stop-color="var(--pine-light)"/>
      </linearGradient>
    </defs>
    <path fill="url(#pine)" d="M0 0H1200V437C1180 400 1165 360 1150 330C1120 270 1090 240 1040 235C990 230 950 250 900 240C850 230 800 250 750 265C700 280 650 255 600 262C550 270 500 250 450 255C400 262 350 240 300 225C260 215 220 215 185 235C140 260 110 320 80 370C55 405 30 430 0 433Z"/>
  </svg>

  <p class="line hosts">SUMMIT BRIGHTWAY REALTY GROUP &amp; GREENLEAF LENDING SERVICES, INC.</p>
  <p class="line presents">PRESENTS</p>
  <h1 class="line annual">ANNUAL</h1>
  <p class="line holiday">Holiday</p>
  <p class="line celebration">CELEBRATION</p>

  <div class="rule top"></div>
  <p class="line audience">FOR AGENTS, ORIGINATORS, CLIENTS &amp; FRIENDS<br>ALL ARE WELCOME</p>
  <div class="rule bottom"></div>

  <p class="line catering">CATERED BY <span class="chef">CHEF RAMO RAMO</span></p>
  <p class="line music">W/ DJ AND FULL DANCE FLOOR</p>

  <p class="line admission">NO COVER CHARGE<span class="stars">★ ★ ★ ★</span>7 PM – 11 PM</p>
  <p class="line venue">at Velvet Parlor 4871 Q Street NE Washington DC 20019</p>
  <p class="line date"><span class="star">★</span>SATURDAY, JANUARY 22, 2022<span class="star">★</span></p>

  <div class="partner lending"><span class="dot"></span>Greenleaf Lending Services, Inc.</div>
  <div class="partner realty"><span class="dot"></span>Summit Brightway Realty Group</div>

  <div class="contact">
    <p class="name">Call Marcus Pelletier</p>
    <p class="phone">at (240) 555-0184 with questions.</p>
  </div>

  <svg class="chef-photo" viewBox="0 0 294 347" role="img" aria-label="Photo of the event chef in a white chef's jacket">
    <defs>
      <linearGradient id="photo" x1="0" y1="0" x2="0" y2="1">
        <stop offset="0" stop-color="var(--photo-cool)"/>
        <stop offset="0.55" stop-color="var(--photo-warm)"/>
        <stop offset="1" stop-color="#e6ddd1"/>
      </linearGradient>
    </defs>
    <path fill="url(#photo)" d="M95 45C95 10 175 0 195 35L200 140C240 150 270 170 272 200L272 347L0 347L0 262C20 222 60 182 88 152Z"/>
  </svg>
</main>
</body>
</html>
```